Infographic for a Life Transformation brand to showcase their principle method

I need a clean infographic which would be used in a brochure to show the 5 steps to achieving a Inner Uprising. (ie Life transformation). I use the theme of a revolution so I would like the graphic to include a raised fist or something to represent a revolution and then the 5 points of information to represent each step.
Needs to very clean and simple. I don't want something that would take up a full page, I want it as a graphic, almost like a big logo. I don't want it laid out like a process chart.

My brand personalities from https://markcharacterhub.com.au/ are
The Everyman and The Magician to give you an idea of my brand.

I've attached my logo so that you can see the colour of it. Graphic doesn't need to match logo but should align with that colour.

Target Market(s)

Top Tier Executives, males, 35-55y old

Industry/Entity Type

Life Coaching

Requirements
Must have
• The graphic must have the 5 Steps: in this order
1.Clarity
2. Measurement
3. Discipline
4. Nutrition
5.Exercise
Nice to have
• It could include these action steps which line up with the 5 steps, It may be too much information by there is the option to include if it works.
1.see it
2. track it
3. do it
4. eat it
5. move it

```html
<!DOCTYPE html>
<html lang="en">
<head>
<meta charset="utf-8">
<title>Inner Uprising – Five Steps</title>
<link href="https://fonts.googleapis.com/css2?family=Saira+Semi+Condensed:wght@500;600;700&display=swap" rel="stylesheet">
<style>
  :root {
    --brand-blue: #0f4c8f;
    --charcoal: #454545;
    --ink: #3f3f3f;
    --paper-top: #fafafa;
    --paper-bottom: #f2f2f2;
    --white: #ffffff;
  }
  html, body { margin: 0; padding: 0; overflow: hidden; }
  body { width: 1197px; height: 1200px; background: var(--paper-bottom); }
  .infographic { display: block; width: 1197px; height: 1200px; font-family: "Saira Semi Condensed", sans-serif; }
  .step-number { font-size: 36px; font-weight: 700; fill: var(--ink); text-anchor: middle; }
  .step-title { font-size: 34px; font-weight: 600; fill: var(--ink); text-anchor: middle; letter-spacing: 0.5px; }
  .brand-name { font-size: 30px; font-weight: 600; fill: var(--white); text-anchor: middle; letter-spacing: 1px; }
  .action-label { font-size: 26px; font-weight: 600; fill: var(--white); text-anchor: middle; letter-spacing: 0.5px; }
  .connector { stroke: var(--charcoal); stroke-width: 1.6; stroke-dasharray: 5 5; fill: none; }
  .node-dot { fill: var(--charcoal); }
  .cycle-ring { fill: none; stroke: var(--charcoal); stroke-width: 3; }
  .cycle-arrow { fill: var(--charcoal); }
  .step-disc { fill: var(--brand-blue); }
  .step-inner-line { fill: none; stroke: var(--white); stroke-width: 3; }
  .step-arc { fill: none; stroke: var(--charcoal); stroke-width: 2.5; stroke-dasharray: 380 154; }
  .step-icon { fill: none; stroke: var(--white); stroke-width: 3; stroke-linecap: round; stroke-linejoin: round; }
  .action-disc { fill: var(--charcoal); }
  .action-ring-solid { fill: none; stroke: var(--brand-blue); stroke-width: 2.5; }
  .action-ring-dashed { fill: none; stroke: var(--brand-blue); stroke-width: 2.5; stroke-dasharray: 7 5; }
  .action-icon { fill: none; stroke: var(--white); stroke-width: 3; stroke-linecap: round; stroke-linejoin: round; }
  .flow-arrow { fill: var(--brand-blue); }
</style>
</head>
<body>
<svg class="infographic" viewBox="0 0 1197 1200" xmlns="http://www.w3.org/2000/svg">
  <defs>
    <linearGradient id="upper-panel" x1="0" y1="0" x2="0" y2="1">
      <stop offset="0" stop-color="#f7f7f7"/>
      <stop offset="1" stop-color="#fbfbfb"/>
    </linearGradient>
  </defs>

  <rect x="0" y="0" width="1197" height="1200" fill="var(--paper-bottom)"/>
  <rect class="upper-panel" x="0" y="26" width="1197" height="861" fill="url(#upper-panel)"/>
  <rect class="top-band" x="0" y="0" width="1197" height="26" fill="var(--brand-blue)"/>

  <g class="connectors">
    <line class="connector" x1="598" y1="348" x2="598" y2="461"/>
    <line class="connector" x1="799" y1="412" x2="711" y2="500"/>
    <line class="connector" x1="780" y1="644" x2="870" y2="644"/>
    <line class="connector" x1="324" y1="644" x2="411" y2="644"/>
    <line class="connector" x1="374" y1="414" x2="478" y2="500"/>
    <circle class="node-dot" cx="598" cy="348" r="6"/><circle class="node-dot" cx="598" cy="461" r="6"/>
    <circle class="node-dot" cx="799" cy="412" r="6"/><circle class="node-dot" cx="711" cy="500" r="6"/>
    <circle class="node-dot" cx="780" cy="644" r="6"/><circle class="node-dot" cx="870" cy="644" r="6"/>
    <circle class="node-dot" cx="324" cy="644" r="6"/><circle class="node-dot" cx="411" cy="644" r="6"/>
    <circle class="node-dot" cx="374" cy="414" r="6"/><circle class="node-dot" cx="478" cy="500" r="6"/>
  </g>

  <g class="core">
    <circle class="cycle-ring" cx="598" cy="644" r="184"/>
    <g class="cycle-arrows">
      <path class="cycle-arrow" d="M9 0 L-9 -9 L-9 9 Z" transform="translate(598 644) rotate(-96.6) translate(184 0) rotate(90)"/>
      <path class="cycle-arrow" d="M9 0 L-9 -9 L-9 9 Z" transform="translate(598 644) rotate(-59.5) translate(184 0) rotate(90)"/>
      <path class="cycle-arrow" d="M9 0 L-9 -9 L-9 9 Z" transform="translate(598 644) rotate(-9.5) translate(184 0) rotate(90)"/>
      <path class="cycle-arrow" d="M9 0 L-9 -9 L-9 9 Z" transform="translate(598 644) rotate(171) translate(184 0) rotate(90)"/>
      <path class="cycle-arrow" d="M9 0 L-9 -9 L-9 9 Z" transform="translate(598 644) rotate(-138.4) translate(184 0) rotate(90)"/>
    </g>
    <circle cx="598" cy="644" r="167" fill="var(--charcoal)"/>
    <text class="brand-name" x="598" y="654">INNER UPRISING</text>
  </g>

  <!-- 1 clarity -->
  <g class="step step-clarity">
    <circle class="step-arc" cx="598" cy="261" r="85" transform="rotate(-150 598 261)"/>
    <circle class="step-disc" cx="598" cy="261" r="77"/>
    <circle class="step-inner-line" cx="598" cy="261" r="69"/>
    <g class="step-icon" transform="translate(598 261)">
      <rect x="-18" y="-34" width="62" height="44" rx="4"/>
      <path d="M-18 -26 L44 -26 M-12 -30 L-10 -30 M-6 -30 L-4 -30 M10 -2 L36 -2 M14 -10 L36 -10"/>
      <circle cx="-14" cy="4" r="20" fill="var(--brand-blue)"/>
      <circle cx="-14" cy="4" r="13"/>
      <path d="M-28 18 L-44 34"/>
    </g>
    <text class="step-number" x="598" y="114">- 1 -</text>
    <text class="step-title" x="598" y="154">CLARITY</text>
  </g>

  <!-- 2 measurement -->
  <g class="step step-measurement">
    <circle class="step-arc" cx="870" cy="360" r="85" transform="rotate(100 870 360)"/>
    <circle class="step-disc" cx="870" cy="360" r="77"/>
    <circle class="step-inner-line" cx="870" cy="360" r="69"/>
    <g class="step-icon" transform="translate(870 360)">
      <path d="M-36 34 L36 34 L36 -24 Z M14 22 L26 22 L26 10 Z"/>
      <g transform="rotate(-35)">
        <rect x="-40" y="-26" width="70" height="20" rx="2"/>
        <path d="M-32 -6 L-32 -13 M-24 -6 L-24 -11 M-16 -6 L-16 -13 M-8 -6 L-8 -11 M0 -6 L0 -13 M8 -6 L8 -11 M16 -6 L16 -13"/>
      </g>
    </g>
    <text class="step-number" x="975" y="469">- 2 -</text>
    <text class="step-title" x="975" y="508">MEASUREMENT</text>
  </g>

  <!-- 3 discipline -->
  <g class="step step-discipline">
    <circle class="step-arc" cx="959" cy="644" r="85" transform="rotate(100 959 644)"/>
    <circle class="step-disc" cx="959" cy="644" r="77"/>
    <circle class="step-inner-line" cx="959" cy="644" r="69"/>
    <g class="step-icon" transform="translate(959 644)">
      <rect x="-36" y="-34" width="72" height="46" rx="3"/>
      <path d="M-14 -12 L-4 -2 L16 -22 M0 12 L0 20 M-20 38 L0 20 L20 38 M-44 -34 L44 -34"/>
    </g>
    <text class="step-number" x="988" y="789">- 3 -</text>
    <text class="step-title" x="988" y="828">DISCIPLINE</text>
  </g>

  <!-- 4 nutrition -->
  <g class="step step-nutrition">
    <circle class="step-arc" cx="238" cy="644" r="85" transform="rotate(-10 238 644)"/>
    <circle class="step-disc" cx="238" cy="644" r="77"/>
    <circle class="step-inner-line" cx="238" cy="644" r="69"/>
    <g class="step-icon" transform="translate(238 644)">
      <path d="M0 -22 C-14 -32 -40 -26 -40 4 C-40 28 -20 42 -8 38 C-4 36 4 36 8 38 C20 42 40 28 40 4 C40 -26 14 -32 0 -22 Z"/>
      <path d="M0 -22 C0 -30 4 -38 10 -42 M4 -30 C10 -42 22 -44 28 -40 C22 -30 12 -28 4 -30 Z"/>
      <path d="M-36 -4 L26 26 M-40 6 L22 36 M-26 1 L-28 6 M-16 6 L-18 11 M-6 11 L-8 16 M4 16 L2 21"/>
    </g>
    <text class="step-number" x="191" y="789">- 4 -</text>
    <text class="step-title" x="191" y="828">NUTRITION</text>
  </g>

  <!-- 5 exercise -->
  <g class="step step-exercise">
    <circle class="step-arc" cx="304" cy="360" r="85" transform="rotate(-10 304 360)"/>
    <circle class="step-disc" cx="304" cy="360" r="77"/>
    <circle class="step-inner-line" cx="304" cy="360" r="69"/>
    <g class="step-icon" transform="translate(304 360) rotate(-45)">
      <rect x="-20" y="-4" width="40" height="8"/>
      <rect x="-36" y="-22" width="16" height="44" rx="2"/>
      <rect x="20" y="-22" width="16" height="44" rx="2"/>
      <rect x="-48" y="-14" width="12" height="28" rx="2"/>
      <rect x="36" y="-14" width="12" height="28" rx="2"/>
    </g>
    <text class="step-number" x="186" y="469">- 5 -</text>
    <text class="step-title" x="186" y="508">EXERCISE</text>
  </g>

  <!-- action row -->
  <g class="actions">
    <g class="action" transform="translate(167 1041)">
      <path class="action-ring-solid" d="M-98 0 A98 98 0 0 1 98 0"/>
      <path class="action-ring-dashed" d="M98 0 A98 98 0 0 1 -98 0"/>
      <circle class="action-disc" r="87"/>
      <path class="action-icon" d="M-33 -22 Q0 -50 33 -22 Q0 6 -33 -22 Z"/>
      <circle class="action-icon" cx="0" cy="-22" r="10"/>
      <text class="action-label" y="40">SEE IT</text>
    </g>
    <path class="flow-arrow" d="M268 1032 L280 1041 L268 1050 Z"/>
    <g class="action" transform="translate(372 1041)">
      <path class="action-ring-solid" d="M-98 0 A98 98 0 0 1 98 0"/>
      <path class="action-ring-dashed" d="M98 0 A98 98 0 0 1 -98 0"/>
      <circle class="action-disc" r="87"/>
      <path class="action-icon" d="M-19 -24 L-26 -34 A9 9 0 1 1 -12 -34 Z"/>
      <path class="action-icon" d="M-19 -20 Q-19 -12 -8 -12 L4 -12 Q12 -12 12 -6 Q12 0 4 0 L-20 0 Q-26 0 -26 -6"/>
      <path class="action-icon" d="M20 -3 L14 -12 A8 8 0 1 1 26 -12 Z"/>
      <text class="action-label" y="40">TRACK IT</text>
    </g>
    <path class="flow-arrow" d="M473 1032 L485 1041 L473 1050 Z"/>
    <g class="action" transform="translate(577 1041)">
      <path class="action-ring-solid" d="M-98 0 A98 98 0 0 1 98 0"/>
      <path class="action-ring-dashed" d="M98 0 A98 98 0 0 1 -98 0"/>
      <circle class="action-disc" r="87"/>
      <rect class="action-icon" x="-21" y="-55" width="42" height="54" rx="4"/>
      <path class="action-icon" d="M-8 -58 L8 -58 L8 -52 L-8 -52 Z M-14 -42 l3 3 l5 -6 M-1 -41 L13 -41 M-14 -30 l3 3 l5 -6 M-1 -29 L13 -29 M-14 -18 l3 3 l5 -6 M-1 -17 L13 -17"/>
      <text class="action-label" y="40">DO IT</text>
    </g>
    <path class="flow-arrow" d="M678 1032 L690 1041 L678 1050 Z"/>
    <g class="action" transform="translate(781 1041)">
      <path class="action-ring-solid" d="M-98 0 A98 98 0 0 1 98 0"/>
      <path class="action-ring-dashed" d="M98 0 A98 98 0 0 1 -98 0"/>
      <circle class="action-disc" r="87"/>
      <path class="action-icon" d="M-28 -50 L-14 -36 M-22 -55 L-9 -42 M-18 -36 L28 -4 M-34 -44 L-20 -30"/>
      <ellipse class="action-icon" cx="20" cy="-44" rx="9" ry="13" transform="rotate(40 20 -44)"/>
      <path class="action-icon" d="M12 -36 L-26 -4"/>
      <text class="action-label" y="40">EAT IT</text>
    </g>
    <path class="flow-arrow" d="M883 1032 L895 1041 L883 1050 Z"/>
    <g class="action" transform="translate(986 1041)">
      <path class="action-ring-solid" d="M-98 0 A98 98 0 0 1 98 0"/>
      <path class="action-ring-dashed" d="M98 0 A98 98 0 0 1 -98 0"/>
      <circle class="action-disc" r="87"/>
      <path class="action-icon" d="M0 -60 L0 -4 M-28 -32 L28 -32 M-8 -52 L0 -60 L8 -52 M-8 -12 L0 -4 L8 -12 M-20 -40 L-28 -32 L-20 -24 M20 -40 L28 -32 L20 -24"/>
      <text class="action-label" y="40">MOVE IT</text>
    </g>
    <path class="flow-arrow" d="M1090 1030 L1104 1041 L1090 1052 Z"/>
  </g>
</svg>
</body>
</html>
```